Tourism Marketing needing sleek, clear design for business card & proposal documents.

***Company background***
"Quiet Harbour" is a company specializing in tourism marketing and project management. We do international wholesale, event management as well as ongoing representation of tourism and hospitality companies.

***Target market***
We cater to tourism companies and hotel professionals.

***Task***
We would like to get a single sided business card designed (but will still consider two sided, we are open to any ideas you may have). The layout for this card should be modern and elegant. Currently we do not have a logo, but we would like our business name in a really simple typography for the business card (similar to Merrow Lounge's logo - www.merrowlounge.com.au).We are after a design that is clear, strong enough to be recognised as Quiet Harbour that does not require any fancy design. Another option is a simple play on QH (Quiet Harbour) or simply have Quiet Harbour featured elsewhere on card more as a brand/logo.

Feel free to submit different fonts if you feel you have any other fonts/designs that may be suitable for this card other than sans serifs. Should this project be successful, we will be considering several other projects for business proposal templates and eventually a website design.

The information that needs to go on the card are as follows:

Odette Farrow
Director
Quiet Harbour
Tourism Marketing & Representation
57 Wendlow Terrace
Larkmoor, Victoria, 3194 Australia
T +61 428306172 E odette@quietharbour.com.au

***Look and feel***
We'd like the business card design to express the following:
Modern, sleek, elegant, simple, discreet, quality, subtle, professional, creative, innovation

In terms of typography, we like something really simple and blocky (similar font to Merrow Lounge's logo - www.merrowlounge.com.au)

***Colour scheme***
Shades of grey and dark teal

***Note***
Although our main target market are professionals, we would like the business card design to be versatile enough to be used outside of the tourism industry and need to appeal to different markets.

I do not have existing logo. Was hoping for a design that may be clear, strong enough not to require one. Other option is a simple play on QH (Quiet Harbour) or simply have Quiet Harbour featured elsewhere on card more as a brand/logo.

Odette Farrow
Director
Quiet Harbour Pty Ltd 
57 Wendlow Terrace
T +61 428306172  E  odette@quietharbour.com.au

Thank you for designs so far. Many have used a mauve colour which matches our company profile. This is not necessary, as that is just a draft and will be completely redesigned, so dont  feel you need to incorporate the mauve.

My colour preferences are for a white or grey background, and I like fonts in dark teals, grey or other sophisticated but modern colours. feel free to submit different fonts if you you have other fonts you thing would be suitable for this card, along with sans serifs. Should this project be successful, we will be considering several others for business proposal templates and eventually website. 

Target Market(s)

International Hospitality Senior Executives, Directors of International Tourism Companies, Directors of Tourism Bodies Internationally, local Tourism

Industry/Entity Type

Hospitality

Requirements
Should not have
• must not have bright garish colour, swirly patterns or anything that dates too much.

```html
<!DOCTYPE html>
<html lang="en">
<head>
<meta charset="utf-8">
<title>Quiet Harbour Pty Ltd – Business Card</title>
<link rel="stylesheet" href="https://fonts.googleapis.com/css2?family=Inter:wght@300;400&family=Open+Sans:wght@400&display=swap">
<style>
  :root {
    --bleed-grey: #bfbdbd;
    --bleed-label: #ffffff;
    --card-white: #ffffff;
    --ink: #454545;
    --petal-rose: #df8f95;
    --petal-terracotta: #d4806c;
    --petal-apricot: #f7b57c;
    --petal-sage: #b6d08e;
    --petal-teal: #74a69a;
  }
  * { margin: 0; padding: 0; box-sizing: border-box; }
  html, body {
    width: 1200px;
    height: 720px;
    overflow: hidden;
    background: var(--bleed-grey);
  }
  .sheet {
    position: relative;
    width: 1200px;
    height: 720px;
    background: var(--bleed-grey);
    font-family: "Inter", "Helvetica Neue", Arial, sans-serif;
  }
  .bleed-label {
    position: absolute;
    font-family: "Open Sans", Arial, sans-serif;
    font-size: 19px;
    letter-spacing: 1px;
    color: var(--bleed-label);
    line-height: 1;
    white-space: nowrap;
    transform: translate(-50%, -50%);
  }
  .bleed-label--side {
    transform: translate(-50%, -50%) rotate(-90deg);
  }
  .card {
    position: absolute;
    left: 40px;
    top: 40px;
    width: 1120px;
    height: 640px;
    background: var(--card-white);
    overflow: hidden;
    color: var(--ink);
  }
  .card__line {
    position: absolute;
    line-height: 1;
    white-space: nowrap;
  }
  .company-name {
    left: 0; right: 0;
    top: 41px;
    text-align: center;
    font-size: 40px;
    font-weight: 400;
  }
  .company-tagline {
    left: 0; right: 0;
    top: 100px;
    text-align: center;
    font-size: 31px;
    font-weight: 300;
  }
  .person-name {
    left: 37px;
    top: 230px;
    font-size: 38px;
    font-weight: 400;
  }
  .person-role {
    left: 37px;
    top: 284px;
    font-size: 35px;
    font-weight: 300;
  }
  .contact {
    left: 37px;
    font-size: 31px;
    font-weight: 300;
  }
  .contact--street { top: 411px; }
  .contact--city   { top: 459px; }
  .contact--phone  { top: 507px; }
  .contact--email  { top: 555px; }
  .contact__key { margin-right: 6px; }
  .petal-artwork {
    position: absolute;
    left: 667px;
    top: 125px;
    width: 453px;
    height: 515px;
    border-top-left-radius: 100% 90%;
    background:
      linear-gradient(180deg, rgba(255,255,255,0.55) 0%, rgba(255,255,255,0) 45%),
      linear-gradient(100deg,
        var(--petal-rose) 0%,
        var(--petal-terracotta) 22%,
        var(--petal-apricot) 45%,
        var(--petal-sage) 72%,
        var(--petal-teal) 100%);
    opacity: 0.9;
  }
</style>
</head>
<body>
  <main class="sheet">
    <span class="bleed-label" style="left:390px; top:21px;">edge out area</span>
    <span class="bleed-label" style="left:603px; top:21px;">edge out area</span>
    <span class="bleed-label" style="left:816px; top:21px;">edge out area</span>
    <span class="bleed-label bleed-label--side" style="left:19px; top:146px;">edge out area</span>
    <span class="bleed-label bleed-label--side" style="left:19px; top:357px;">edge out area</span>
    <span class="bleed-label bleed-label--side" style="left:19px; top:569px;">edge out area</span>

    <section class="card">
      <div class="petal-artwork" role="img" aria-label="Fan of translucent overlapping leaf shapes in rose, terracotta, apricot, sage green and teal"></div>

      <h1 class="card__line company-name">Quiet Harbour Pty Ltd</h1>
      <p class="card__line company-tagline">Tourism Marketing &amp; Representation</p>

      <p class="card__line person-name">Odette Farrow</p>
      <p class="card__line person-role">Director</p>

      <p class="card__line contact contact--street">57 Wendlow Terrace</p>
      <p class="card__line contact contact--city">Larkmoor, Victoria, 3194 Australia</p>
      <p class="card__line contact contact--phone"><span class="contact__key">T</span>+61 428306172</p>
      <p class="card__line contact contact--email"><span class="contact__key">E</span> odette@quietharbour.com.au</p>
    </section>
  </main>
</body>
</html>
```